Business card based on your logo design "Brennock&Co"

Can you please design a business card based on the logo artwork you designed for our business. Double sided as per your submitted image of possible application of logo.

```html
<!DOCTYPE html>
<html lang="en">
<head>
<meta charset="utf-8">
<title>Brennock&amp;Co Business Card</title>
<link href="https://fonts.googleapis.com/css2?family=Open+Sans:wght@400;600&display=swap" rel="stylesheet">
<style>
  :root {
    --canvas-bg: #e6e4e1;
    --card-dark: #333436;
    --orange-light: #ffb634;
    --orange-deep: #f79800;
    --orange-accent: #f7941d;
    --ink-dark: #323335;
    --white: #ffffff;
    --rule: #77787a;
  }
  * { margin: 0; padding: 0; box-sizing: border-box; }
  html, body { width: 1200px; height: 1024px; overflow: hidden; }
  body {
    background: var(--canvas-bg);
    display: flex;
    flex-direction: column;
    align-items: center;
    justify-content: center;
    gap: 30px;
    font-family: "Open Sans", Arial, sans-serif;
  }
  .card {
    width: 820px;
    height: 469px;
    border-radius: 30px;
    position: relative;
    overflow: hidden;
    box-shadow: 0 6px 18px rgba(0,0,0,0.18);
  }
  .brand-row { display: flex; align-items: center; gap: 12px; }
  .brand-square { flex: none; background: var(--orange-accent); }
  .wordmark {
    font-family: "Open Sans", Arial, sans-serif;
    font-weight: 600;
    line-height: 1;
    white-space: nowrap;
  }
  .tagline {
    font-family: "Open Sans", Arial, sans-serif;
    font-weight: 400;
    white-space: nowrap;
  }

  /* Front */
  .card-front { background: var(--card-dark); color: var(--white); }
  .front-brand {
    position: absolute;
    left: 44px; top: 0; bottom: 0;
    width: 340px;
    display: flex; flex-direction: column; justify-content: center;
  }
  .card-front .brand-square { width: 14px; height: 14px; }
  .card-front .wordmark { font-size: 37px; color: var(--white); }
  .card-front .tagline { font-size: 12px; color: var(--white); margin-top: 10px; letter-spacing: 0.8px; }
  .divider {
    position: absolute;
    left: 410px; top: 60px; bottom: 60px;
    width: 1px; background: var(--rule);
  }
  .person {
    position: absolute;
    left: 440px; right: 50px; top: 60px;
    display: flex; flex-direction: column; align-items: flex-end;
  }
  .person-name-row { display: flex; align-items: center; width: 100%; gap: 14px; }
  .person-name-row::before { content: ""; flex: 1; height: 1px; background: var(--rule); }
  .person-name { font-size: 28px; font-weight: 600; }
  .person-role { font-size: 15px; color: var(--orange-accent); margin-top: 2px; }
  .contacts {
    position: absolute;
    left: 440px; bottom: 58px;
    list-style: none;
    font-size: 17px;
    color: #e8e8e8;
  }
  .contacts li { display: flex; align-items: center; gap: 16px; height: 34px; }
  .contacts svg { width: 18px; height: 18px; fill: none; stroke: var(--orange-accent); stroke-width: 2; }

  /* Back */
  .card-back {
    background: radial-gradient(ellipse at 40% 40%, var(--orange-light), var(--orange-deep));
    display: flex; align-items: center; justify-content: center;
  }
  .card-back .brand-square { width: 26px; height: 26px; background: var(--ink-dark); }
  .card-back .brand-row { gap: 18px; }
  .card-back .wordmark { font-size: 76px; color: var(--ink-dark); }
  .card-back .tagline { font-size: 20px; color: var(--ink-dark); margin-top: 14px; letter-spacing: 2px; }
</style>
</head>
<body>
  <section class="card card-front">
    <div class="front-brand">
      <div class="brand-row">
        <span class="brand-square"></span>
        <span class="wordmark">BRENNOCK&amp;CO</span>
      </div>
      <div class="tagline">Building and Project Management</div>
    </div>
    <div class="divider"></div>
    <div class="person">
      <div class="person-name-row"><span class="person-name">Daniel Hartwell</span></div>
      <div class="person-role">Managing Director</div>
    </div>
    <ul class="contacts">
      <li>
        <svg viewBox="0 0 24 24"><path d="M5 3h4l2 5-3 2a12 12 0 0 0 6 6l2-3 5 2v4a2 2 0 0 1-2 2A18 18 0 0 1 3 5a2 2 0 0 1 2-2z"/></svg>
        <span>0400 555 218</span>
      </li>
      <li>
        <svg viewBox="0 0 24 24"><rect x="3" y="5" width="18" height="14" rx="1"/><path d="M3 6l9 7 9-7"/></svg>
        <span>daniel@brennockco.com</span>
      </li>
      <li>
        <svg viewBox="0 0 24 24"><circle cx="12" cy="12" r="9"/><path d="M3 12h18M12 3c3 3 3 15 0 18M12 3c-3 3-3 15 0 18"/></svg>
        <span>www.brennockco.com</span>
      </li>
    </ul>
  </section>

  <section class="card card-back">
    <div class="back-brand">
      <div class="brand-row">
        <span class="brand-square"></span>
        <span class="wordmark">BRENNOCK&amp;CO</span>
      </div>
      <div class="tagline">Building and Project Management</div>
    </div>
  </section>
</body>
</html>
```